design a construction company business card

Design business card around our logo. Card must have all the typical info: name, title, address, phone, email, business name, etc. Somewhere on the card I would like to see our motto "Built on integrity... Inspired by commitment." Consider adding a splash of bright orange to the card to complement the blues and silvers/grays in the logo. We are open to metallic inks, textures, etc. We would like to see options on both light and dark backgrounds. The font in the logo is Euro Technic Extended Regular.

```html
<!DOCTYPE html>
<html lang="en">
<head>
<meta charset="utf-8">
<title>Halden Building Co. – Business Card</title>
<link href="https://fonts.googleapis.com/css2?family=Roboto:ital,wght@0,400;0,500;0,700;1,400&display=swap" rel="stylesheet">
<style>
  :root {
    --canvas: #2b2b2d;
    --card-dark: #2e2e30;
    --card-light: #ffffff;
    --brand-blue: #1f4fa8;
    --silver: #c9ccd1;
    --ink: #3a3a3c;
    --ink-soft: #55575b;
    --band-dark: #2f2f31;
  }
  * { margin: 0; padding: 0; box-sizing: border-box; }
  html, body {
    width: 1200px; height: 960px; overflow: hidden;
    background: var(--canvas);
    font-family: "Roboto", Arial, sans-serif;
  }
  .canvas { position: relative; width: 1200px; height: 960px; }

  .card {
    position: absolute;
    width: 700px; height: 400px;
    box-shadow: 0 12px 30px rgba(0,0,0,.45);
    overflow: hidden;
  }

  /* Back of card (dark) */
  .card--back { left: 250px; top: 60px; background: var(--card-dark); }
  .card--back .brand {
    position: absolute; left: 0; right: 0; top: 150px;
    text-align: center;
    color: var(--silver);
    font-weight: 700; font-size: 46px; letter-spacing: 4px;
    text-transform: uppercase;
  }
  .card--back .motto {
    position: absolute; left: 0; right: 0; top: 300px;
    text-align: center;
    color: #f2f2f2; font-size: 17px; letter-spacing: .3px;
  }

  /* Front of card (light) */
  .card--front { left: 250px; top: 500px; background: var(--card-light); }
  .person { position: absolute; left: 48px; top: 56px; }
  .person__name { color: var(--brand-blue); font-weight: 700; font-size: 30px; }
  .person__title { color: var(--ink-soft); font-style: italic; font-size: 16px; margin-top: 2px; }

  .address {
    position: absolute; left: 48px; top: 158px;
    color: var(--ink); font-size: 16px; line-height: 22px;
  }
  .contacts {
    position: absolute; left: 48px; top: 222px;
    list-style: none; color: var(--ink); font-size: 17px;
  }
  .contacts li { display: flex; align-items: center; gap: 10px; height: 25px; }
  .contacts svg { width: 15px; height: 15px; fill: var(--brand-blue); flex: none; }

  .brand--front {
    position: absolute; right: 40px; top: 112px;
    display: flex; align-items: center; gap: 12px;
    color: var(--brand-blue);
    font-weight: 700; font-size: 34px; letter-spacing: 2px; text-transform: uppercase;
  }
  .brand__mark { width: 18px; height: 18px; background: var(--brand-blue); }

  .footer-rule { position: absolute; left: 0; right: 0; top: 322px; height: 4px; background: var(--brand-blue); }
  .footer-band { position: absolute; left: 0; right: 0; top: 332px; bottom: 0; background: var(--band-dark); }
</style>
</head>
<body>
<main class="canvas">
  <section class="card card--back" aria-label="Card back">
    <div class="brand">Halden Building Co.</div>
    <p class="motto">Built on integrity... Inspired by commitment</p>
  </section>

  <section class="card card--front" aria-label="Card front">
    <div class="person">
      <h1 class="person__name">Daniel Brooks</h1>
      <p class="person__title">Director</p>
    </div>

    <address class="address" style="font-style:normal">
      Level 2, 57 Harbour Lane<br>Fairview, VIC 3102
    </address>

    <ul class="contacts">
      <li>
        <svg viewBox="0 0 24 24" aria-hidden="true"><path d="M6.6 10.8a15 15 0 0 0 6.6 6.6l2.2-2.2a1 1 0 0 1 1-.25 11.4 11.4 0 0 0 3.6.57 1 1 0 0 1 1 1V20a1 1 0 0 1-1 1A17 17 0 0 1 3 4a1 1 0 0 1 1-1h3.5a1 1 0 0 1 1 1c0 1.25.2 2.45.57 3.6a1 1 0 0 1-.25 1z"/></svg>
        555 014 2286
      </li>
      <li>
        <svg viewBox="0 0 24 24" aria-hidden="true"><path d="M2 5h20v14H2z M2 5l10 8 10-8" /></svg>
        hello@haldenbuild.com
      </li>
      <li>
        <svg viewBox="0 0 24 24" aria-hidden="true"><circle cx="12" cy="12" r="10"/></svg>
        www.haldenbuild.com
      </li>
    </ul>

    <div class="brand--front">
      <span class="brand__mark" aria-hidden="true"></span>
      <span>Halden Building Co.</span>
    </div>

    <div class="footer-rule"></div>
    <div class="footer-band"></div>
  </section>
</main>
</body>
</html>
```